Keystone Tenancy Hour podcast postcard

I've launched a podcast about apartment investing, ownership and management which is newly up on quorl and brevano. I want to create a postcard that I can mail to my client base to get them to subscribe

```html
<!DOCTYPE html>
<html lang="en">
<head>
<meta charset="utf-8">
<title>Keystone Tenancy Hour – Podcast Postcard</title>
<link href="https://fonts.googleapis.com/css2?family=Roboto:ital,wght@0,400;0,500;0,700;0,900;1,900&family=Roboto+Condensed:wght@700&display=swap" rel="stylesheet">
<style>
  :root {
    --page-bg: #e6e7ea;
    --white: #f7f7f7;
    --purple: #33263f;
    --purple-dark: #2c2037;
    --orange: #d68f27;
    --cyan: #5cc6da;
    --ink: #111111;
    --strip-grey: #e3e3e3;
    --photo-light: #e7c98f;
    --photo-mid: #b98a45;
    --photo-dark: #5c4a36;
  }
  * { margin: 0; padding: 0; box-sizing: border-box; }
  html, body {
    width: 1200px; height: 1200px; overflow: hidden;
    background: var(--page-bg);
    font-family: "Roboto", Arial, sans-serif;
  }
  .postcard {
    position: absolute;
    left: 50px; top: 233px;
    width: 1223px; height: 815px;
    transform: scale(0.9);
    transform-origin: 0 0;
    overflow: hidden;
    box-shadow: 0 10px 30px rgba(0,0,0,0.18);
  }
  .postcard__shapes, .postcard__photo {
    position: absolute; left: 0; top: 0; width: 1223px; height: 815px;
  }
  .brand {
    position: absolute; left: 50px; top: 58px;
    line-height: 1;
  }
  .brand__top {
    display: block;
    font-weight: 700; font-size: 48px; letter-spacing: 3px;
    color: var(--ink);
  }
  .brand__bottom {
    display: block; margin-top: 12px;
    font-family: "Roboto Condensed", "Roboto", sans-serif;
    font-weight: 700; font-size: 64px; letter-spacing: 1px;
    color: var(--orange);
  }
  .topics { position: absolute; left: 0; top: 200px; width: 800px; list-style: none; }
  .topic {
    position: absolute; left: 78px;
    display: flex; align-items: center; gap: 24px;
    height: 90px;
  }
  .topic svg { width: 84px; height: 84px; flex: none; }
  .topic__label {
    font-weight: 500; font-size: 53px; color: var(--cyan);
    letter-spacing: 0.5px;
  }
  .topic--investing { top: 27px; }
  .topic--ownership { top: 137px; }
  .topic--management { top: 248px; }
  .pitch {
    position: absolute; left: 48px; top: 612px; width: 455px;
    font-size: 21px; font-weight: 500; line-height: 27px; color: var(--ink);
  }
  .contact {
    position: absolute; right: 42px; top: 609px; text-align: right;
  }
  .contact__note {
    font-size: 21px; font-weight: 500; color: var(--ink); letter-spacing: 0.2px;
  }
  .contact__phone {
    font-weight: 900; font-style: italic; font-size: 86px; line-height: 1;
    color: var(--ink); margin-top: 0;
  }
  .subscribe {
    position: absolute; left: 50px; top: 740px;
    font-size: 54px; line-height: 1; white-space: nowrap;
  }
  .subscribe__label { font-weight: 700; color: #ffffff; }
  .subscribe__where { font-weight: 400; color: var(--cyan); }
</style>
</head>
<body>
  <main class="postcard">
    <svg class="postcard__shapes" viewBox="0 0 1223 815" aria-hidden="true">
      <rect x="0" y="0" width="1223" height="815" fill="var(--white)"/>
      <polygon points="0,200 577,200 826,592 0,592" fill="var(--purple)"/>
      <rect x="0" y="323" width="655" height="4" fill="var(--purple-dark)"/>
      <rect x="0" y="437" width="728" height="4" fill="var(--purple-dark)"/>
      <rect x="0" y="590" width="1223" height="130" fill="var(--strip-grey)"/>
      <polygon points="512,592 1223,592 1223,720 640,720" fill="var(--orange)"/>
      <rect x="0" y="720" width="1223" height="95" fill="var(--purple)"/>
    </svg>

    <svg class="postcard__photo" viewBox="0 0 1223 815" role="img" aria-label="Photo of a sunlit apartment building facade with balconies">
      <defs>
        <linearGradient id="facade" x1="0" y1="0" x2="1" y2="1">
          <stop offset="0" stop-color="var(--photo-dark)"/>
          <stop offset="0.35" stop-color="var(--photo-mid)"/>
          <stop offset="0.7" stop-color="var(--photo-light)"/>
          <stop offset="1" stop-color="var(--photo-mid)"/>
        </linearGradient>
      </defs>
      <polygon points="450,0 1223,0 1223,590 825,590" fill="url(#facade)"/>
      <polygon points="514,100 1223,100 1223,200 577,200" fill="var(--orange)" opacity="0.55"/>
    </svg>

    <h1 class="brand">
      <span class="brand__top">KEYSTONE</span>
      <span class="brand__bottom">TENANCY HOUR</span>
    </h1>

    <ul class="topics">
      <li class="topic topic--investing">
        <svg viewBox="0 0 84 84" aria-hidden="true">
          <circle cx="46" cy="22" r="16" fill="var(--orange)"/>
          <text x="46" y="30" text-anchor="middle" font-family="Roboto, sans-serif" font-weight="700" font-size="22" fill="var(--purple)">$</text>
          <path d="M14 58 L30 48 Q38 44 46 48 L58 52 Q64 54 62 59 Q60 63 54 61 L44 58 L56 62 L72 52 Q78 50 80 55 Q81 59 76 62 L56 74 Q50 77 42 75 L26 70 Z" fill="var(--orange)"/>
          <rect x="4" y="60" width="14" height="6" rx="2" transform="rotate(-35 11 63)" fill="var(--orange)"/>
        </svg>
        <span class="topic__label">INVESTING</span>
      </li>
      <li class="topic topic--ownership">
        <svg viewBox="0 0 84 84" aria-hidden="true">
          <polygon points="42,8 80,40 72,40 72,78 12,78 12,40 4,40" fill="var(--orange)"/>
          <rect x="58" y="10" width="9" height="18" fill="var(--orange)"/>
          <circle cx="42" cy="44" r="8" fill="var(--purple)"/>
          <path d="M28 70 Q28 56 42 56 Q56 56 56 70 Z" fill="var(--purple)"/>
        </svg>
        <span class="topic__label">OWNERSHIP</span>
      </li>
      <li class="topic topic--management">
        <svg viewBox="0 0 84 84" aria-hidden="true">
          <rect x="26" y="10" width="24" height="12" rx="3" fill="none" stroke="var(--orange)" stroke-width="6"/>
          <rect x="4" y="22" width="68" height="46" rx="6" fill="var(--orange)"/>
          <rect x="4" y="40" width="68" height="4" fill="var(--purple)"/>
          <circle cx="64" cy="62" r="17" fill="var(--orange)" stroke="var(--purple)" stroke-width="4"/>
          <text x="64" y="70" text-anchor="middle" font-family="Roboto, sans-serif" font-weight="700" font-size="22" fill="var(--purple)">$</text>
        </svg>
        <span class="topic__label">MANAGEMENT</span>
      </li>
    </ul>

    <p class="pitch">Our new podcast guides you through the process while sharing various ways to maximize your property value!</p>

    <div class="contact">
      <p class="contact__note">NEW PODCAST! GOT A QUESTION FOR THE SHOW? CALL OR TEXT</p>
      <p class="contact__phone">123 456 7890</p>
    </div>

    <p class="subscribe">
      <span class="subscribe__label">SUBSCRIBE NOW : </span><span class="subscribe__where">ON QUORL &amp; BREVANO</span>
    </p>
  </main>
</body>
</html>
```